Aviation: IFR Study Guide Book Cover

We need a book cover (front and back) designed for an Instrument Flight Rules (IFR) study guide used by helicopter and airplane pilots to obtain an instrument rating for a helicopter or airplane. Below is the title and subtitles.

TITLE: IFR STUDY GUIDE
SUBTITLE 1: Checkride Preparation for Airplane and Helicopter Pilots
SUBTITLE 2: Prepare for your Instrument Rating with Confidence

We have also upload recommended text to be included on the back cover. In addition, we included images of similar book covers that we like and ones that we do not like. Below are links to two others books by the author.

https://www.shopvendrix.com/Rotorcraft-Exam-Handbook-oral-flighttest/dp/204715382K
https://www.shopvendrix.com/Manual-Floatcraft-Piloting-Marcus-Holloway/dp/1702538146

Target Market(s)

Flight students

Industry/Entity Type

Aviation

Requirements
Nice to have
• helicopter and airplane

```html
<!DOCTYPE html>
<html lang="en">
<head>
<meta charset="utf-8">
<title>IFR Study Guide – Cover</title>
<link rel="stylesheet" href="https://fonts.googleapis.com/css2?family=Archivo:wght@800&family=Arimo:wght@300;400&family=Open+Sans:ital,wght@0,700;1,700;1,800&display=swap">
<style>
  :root{
    --sky-top:#8fa3b8;
    --sky-mid:#d9b58a;
    --sky-glow:#f3c27a;
    --ground-haze:#6f7a92;
    --ground-deep:#2c3350;
    --panel:rgba(58,64,82,0.72);
    --banner:rgba(88,92,102,0.85);
    --text:#ffffff;
    --rule:#ffffff;
  }
  *{margin:0;padding:0;box-sizing:border-box}
  html,body{width:1200px;height:767px;overflow:hidden;background:#222}
  .cover{position:relative;width:1200px;height:767px;overflow:hidden;color:var(--text);font-family:"Arimo",Arial,sans-serif}
  .cover__scene{position:absolute;inset:0;width:100%;height:100%}
  .back{position:absolute;left:29px;top:35px;width:539px;height:732px;background:var(--panel);padding:0 25px}
  .back__heading{font-family:"Archivo",Arial,sans-serif;font-weight:800;font-size:16px;text-align:center;letter-spacing:.2px}
  .back__heading--first{margin-top:64px}
  .back__text{font-size:13.2px;line-height:16.8px;text-align:justify;margin-top:14px}
  .back__heading--second{margin-top:16px}
  .topics{width:481px;border-collapse:collapse;margin-top:18px}
  .topics td{border:1.5px solid var(--rule);font-weight:300;font-size:13.4px;text-align:center;height:33px;padding:0 4px;white-space:nowrap}
  .author__heading{margin-top:38px}
  .author__text{margin-top:14px;width:489px}
  .author__text--wrap{width:357px;margin-top:0;text-align:left}
  .barcode-area{position:absolute;left:434px;top:660px;width:137px;height:80px;background:#fff}
  .banner{position:absolute;left:568px;top:36px;width:598px;height:31px;background:var(--banner);font-family:"Open Sans",Arial,sans-serif;font-style:italic;font-weight:700;font-size:15.6px;text-align:right;padding-right:15px;line-height:31px;letter-spacing:.2px}
  .front__title{position:absolute;right:134px;top:335px;font-family:"Open Sans",Arial,sans-serif;font-weight:700;font-size:104px;line-height:1;letter-spacing:-2px}
  .front__subtitle{position:absolute;right:132px;top:436px;font-family:"Open Sans",Arial,sans-serif;font-style:italic;font-weight:800;font-size:48px;line-height:1;letter-spacing:-1px}
  .front__tagline{position:absolute;left:700px;width:400px;top:497px;text-align:center;font-family:"Open Sans",Arial,sans-serif;font-style:italic;font-weight:700;font-size:19px;line-height:23px}
  .front__author{position:absolute;right:163px;top:686px;font-family:"Open Sans",Arial,sans-serif;font-style:italic;font-weight:800;font-size:25.5px}
</style>
</head>
<body>
<main class="cover">
  <svg class="cover__scene" viewBox="0 0 1200 767" role="img" aria-label="Photograph of a high-wing single-engine airplane banking over a hazy sunset landscape overlaid with a faded aeronautical chart">
    <defs>
      <linearGradient id="sky" x1="0" y1="0" x2="0" y2="1">
        <stop offset="0" stop-color="var(--sky-top)"/>
        <stop offset="0.3" stop-color="var(--sky-mid)"/>
        <stop offset="0.45" stop-color="var(--sky-glow)"/>
        <stop offset="0.62" stop-color="var(--ground-haze)"/>
        <stop offset="1" stop-color="var(--ground-deep)"/>
      </linearGradient>
    </defs>
    <rect width="1200" height="767" fill="url(#sky)"/>
  </svg>

  <section class="back">
    <h2 class="back__heading back__heading--first">Prepare for your IFR check ride with confidence</h2>
    <p class="back__text">Becoming an instrument rated pilot is one of the most challenging ratings to obtain. This guide helps prepare you to pass your IFR check ride with confidence. The question-and-answer format is easy to follow and provides detailed explanations for expanded knowledge.</p>
    <h2 class="back__heading back__heading--second">Includes Helicopter and Airplane Specific Content</h2>
    <p class="back__text">This guide is designed to prepare an airplane or helicopter pilot the oral portion of the IFR checkride. Unlike other resources, this guide specifically addresses the differences with IFR flight in helicopters. As a dual rated pilot, the author ensures to identify areas of differences between the two categories of IFR flight. The following concepts are addressed within the guide.</p>
    <table class="topics">
      <tr><td>Preflight Actions</td><td>Enroute Procedures</td><td>Aeromedical Factors</td></tr>
      <tr><td>General IFR Concepts</td><td>Approach Procedures</td><td>Weather Fundamentals</td></tr>
      <tr><td>Departure Procedures</td><td>IFR Emergences</td><td>Risk Management</td></tr>
    </table>
    <h2 class="back__heading author__heading">ABOUT THE AUTHOR:</h2>
    <p class="back__text author__text">Marcus Holloway is ATP rated pilot and helicopter and fixed-wing instructor. Marcus is the owner and operator Tallgrass Meridian, LLC which does business as Vantor Aviation and Pelican Float Air. Vantor Aviation provides primary helicopter flight instruction while Pelican Float Air provides seaplane flight instruction and tours. In addition to instructing, Marcus has authored other books to include The Rotorcraft Exam Handbook, and Manual of Floatcraft Piloting. Marcus lives in Kentucky with his beautiful wife Renata. They have a daughter, Clara, that is dual rated and employed as a captain for a charter company.</p>
    <p class="back__text author__text author__text--wrap">Prior to learning to fly, Marcus spent several years in the military as a Special Warfare Combat Craft Crewman in the U.S. Navy and Ranger-qualified infantry officer in the U.S. Army.</p>
  </section>
  <div class="barcode-area"></div>

  <p class="banner">PREPARE FOR YOUR INSTRUMENT RATING WITH CONFIDENCE</p>
  <h1>
    <span class="front__title">IFR</span>
    <span class="front__subtitle">STUDY GUIDE</span>
  </h1>
  <p class="front__tagline">CHECKRIDE PREPARATION FOR AIRPLANE AND HELICOPTER PILOTS</p>
  <p class="front__author">MARCUS R. HOLLOWAY</p>
</main>
</body>
</html>
```